We need a Word Template for Custom Laboratory Results from an independent laboratory

The test is a novel biomarker for a chronic pain condition called endometriosis. It is expressed as a percentage. We will upload a sample result. We are looking for improved graphic fidelity with more attention to design and spacing. Emphasis should be placed on the overall result, i.e. the patient percentage results. Considerationis going to be given to the most appealing graphic result.

Target Market(s)

Women aged 19-45

Colors
0054AA
0677BA
7BADD7
CADEEF
E8F1F8

```html
<!DOCTYPE html>
<html lang="en">
<head>
<meta charset="utf-8">
<title>Endometriosis Assay Result Template</title>
<link href="https://fonts.googleapis.com/css2?family=Merriweather:wght@400;700&family=Poppins:wght@400&display=swap" rel="stylesheet">
<style>
  :root{
    --brand-blue:#3a5fab;
    --brand-light:#7b9fd4;
    --ink:#1a1a1a;
    --backdrop:#f3f3f5;
    --paper:#ffffff;
  }
  html,body{margin:0;padding:0;width:861px;height:1200px;overflow:hidden;background:var(--backdrop);}
  .report{
    position:absolute;left:20px;top:70px;width:820px;height:1060px;
    background:var(--paper);font-family:'Merriweather',Georgia,serif;color:var(--ink);
    overflow:hidden;box-shadow:0 1px 4px rgba(0,0,0,.06);
  }
  .report__topbar{position:absolute;left:0;top:0;width:100%;height:17px;background:var(--brand-blue);}
  .lab-name{position:absolute;left:62px;top:62px;font-size:40px;font-weight:700;color:var(--brand-blue);letter-spacing:-.5px;}
  .clinic-name{position:absolute;right:56px;top:64px;text-align:left;font-size:22px;font-weight:400;color:var(--brand-blue);line-height:1.2;}
  .header-rule{position:absolute;left:49px;top:165px;width:731px;height:2px;background:var(--brand-blue);}
  .report__title{position:absolute;left:0;top:208px;width:100%;text-align:center;font-size:22px;font-weight:700;line-height:28px;margin:0;}
  .patient{position:absolute;left:73px;top:333px;font-size:15.5px;line-height:25px;}
  .patient__row{display:flex;}
  .patient__label{width:241px;}
  .result__heading{position:absolute;left:0;top:505px;width:100%;text-align:center;font-size:16px;font-weight:700;color:var(--brand-blue);margin:0;}
  .result__table{position:absolute;left:139px;top:545px;width:540px;height:84px;border:1.5px solid var(--ink);display:flex;box-sizing:border-box;}
  .result__label{width:270px;border-right:1.5px solid var(--ink);padding:15px 14px;box-sizing:border-box;font-size:12.5px;line-height:16px;white-space:nowrap;}
  .result__value{flex:1;display:flex;align-items:center;justify-content:center;font-size:34px;font-weight:700;color:var(--brand-blue);}
  .reference{position:absolute;left:82px;top:704px;font-size:13px;line-height:16px;}
  .reference__title{color:var(--brand-blue);font-weight:700;text-decoration:underline;margin-bottom:7px;}
  .reference__row{display:flex;}
  .reference__range{width:97px;}
  .footer-wave{position:absolute;left:0;bottom:0;width:820px;height:90px;}
  .footer-url{position:absolute;right:37px;bottom:28px;font-family:'Poppins',Arial,sans-serif;font-size:15.5px;color:var(--paper);}
</style>
</head>
<body>
  <main class="report">
    <div class="report__topbar"></div>
    <div class="lab-name">Veloria</div>
    <div class="clinic-name">Harbourline<br>Fertility</div>
    <div class="header-rule"></div>

    <h1 class="report__title">ENDOVA MICRO-RNA<br>ENDOMETRIOSIS ASSAY</h1>

    <section class="patient">
      <div class="patient__row"><span class="patient__label">Last Name, First Name</span><span>: John Doe</span></div>
      <div class="patient__row"><span class="patient__label">OHIP Number (12 Character)</span><span>: 123456789101</span></div>
      <div class="patient__row"><span class="patient__label">DOB</span><span>: December 31, 1999</span></div>
    </section>

    <h2 class="result__heading">YOUR RESULT</h2>
    <div class="result__table">
      <div class="result__label">Predicted Probability of Endometriosis<br>Compared to Surgical Controls<br>(100% probability)</div>
      <div class="result__value">37%</div>
    </div>

    <section class="reference">
      <div class="reference__title">Reference Range:</div>
      <div class="reference__row"><span class="reference__range">0.0-29.9%</span><span>Low probability of endometriosis</span></div>
      <div class="reference__row"><span class="reference__range">29.9-44.9%</span><span>Inconclusive</span></div>
      <div class="reference__row"><span class="reference__range">45.0-55.0%</span><span>Intermediate risk of endometriosis</span></div>
      <div class="reference__row"><span class="reference__range">55.1-64.9%</span><span>Probable endometriosis</span></div>
      <div class="reference__row"><span class="reference__range">65.0-99.9%</span><span>Highly probable endometriosis</span></div>
    </section>

    <svg class="footer-wave" viewBox="0 0 820 90" preserveAspectRatio="none">
      <path d="M0 17 C120 40 240 55 360 58 C480 60 600 20 700 5 C750 -2 790 2 820 10 L820 90 L0 90 Z" fill="var(--brand-light)"/>
      <path d="M0 28 C120 50 240 62 360 63 C480 64 600 22 700 7 C750 0 790 4 820 12 L820 90 L0 90 Z" fill="var(--brand-blue)"/>
    </svg>
    <div class="footer-url">www.harbourlinefertility.com</div>
  </main>
</body>
</html>
```